Corporate Profile, with ALOT more work for winning bidder

We need
1. CD designed
2. CD Cover Designed
3. 2x Envelope's designed
4. Letter head designed
The designer picked will also get many further projects from us. Almost totaling 10k a year.
- More info
• Software installation disc
a. Logo
b. Contact details (See below)
c. Instructions
o “Please insert CD into computer and follow the prompts”
d. Title
o “Free Software Installation Disc”
• CD Sleave double sided
- Front
o Logo
o Website Address
o Facebook address
o Title
? “Free Software Installation Disc”
• Letter head
- Logo
- Contact information
- A4 paper size
• C4 Envelope
- Nicely Designed with logo
- A window to put address
- Printed return address (See below) on back
• DL Envelope, to return to us
- Had our return address ( See below)
- Nice design
Contact details
Pixel Harbour Co
17b Tamsin Crescent Larkfield, Vic, 3921
www.PixelHarbourCo.com.au
1300 42 19 58
www.Chatterloop.com/PixelHarbourCo
Return Address
Pixel Harbour Co
17b Tamsin Crescent
Larkfield, Vic, 3921

```html
<!DOCTYPE html>
<html lang="en">
<head>
<meta charset="utf-8">
<title>Pixel Harbour Co — Letterhead</title>
<link href="https://fonts.googleapis.com/css2?family=Roboto:wght@400;700;900&display=swap" rel="stylesheet">
<style>
  :root {
    --paper: #ffffff;
    --cyan: #52e4f2;
    --navy: #1b3f8f;
    --ink: #1c2b3a;
    --rule: #2c8fa6;
  }
  html, body {
    margin: 0;
    padding: 0;
    overflow: hidden;
    background: var(--paper);
  }
  .letterhead {
    position: relative;
    width: 872px;
    height: 1200px;
    background: var(--paper);
    overflow: hidden;
    font-family: "Roboto", Arial, sans-serif;
  }
  .side-band {
    position: absolute;
    top: 0;
    left: 0;
  }
  .brand {
    position: absolute;
    top: 58px;
    left: 600px;
    width: 192px;
    text-align: center;
  }
  .brand-dot {
    display: block;
    width: 70px;
    height: 70px;
    margin: 0 auto 16px;
    border-radius: 50%;
    background: var(--navy);
  }
  .brand-name {
    font-weight: 900;
    font-size: 21px;
    line-height: 24px;
    letter-spacing: -0.4px;
    color: var(--navy);
    white-space: nowrap;
  }
  .contact {
    position: absolute;
    top: 212px;
    left: 608px;
    width: 180px;
    font-style: normal;
    font-size: 9px;
    line-height: 12px;
    color: var(--ink);
  }
  .contact-group {
    padding: 5px 0;
    border-bottom: 1px solid var(--rule);
  }
  .contact-group:last-child {
    border-bottom: none;
  }
  .contact p {
    margin: 0;
    white-space: nowrap;
  }
</style>
</head>
<body>
  <main class="letterhead">
    <svg class="side-band" width="872" height="1200" viewBox="0 0 872 1200" aria-hidden="true">
      <polygon points="598,0 872,0 872,585 598,530" fill="var(--cyan)"/>
    </svg>

    <header class="brand">
      <span class="brand-dot"></span>
      <div class="brand-name">PIXEL HARBOUR CO</div>
    </header>

    <address class="contact">
      <div class="contact-group">
        <p>17b Tamsin Crescent</p>
        <p>Larkfield, Vic, 3921</p>
      </div>
      <div class="contact-group">
        <p>www.PixelHarbourCo.com.au</p>
        <p>www.Chatterloop.com/PixelHarbourCo</p>
      </div>
      <div class="contact-group">
        <p>1300 42 19 58</p>
      </div>
    </address>
  </main>
</body>
</html>
```